Bakery needs an eye catching packaging design for a new budget pie!

Hi all and welcome to this project! Looking for a playful, bright, graphic packaging design for our pie called the ‘Velkoro Scholar Pie’.

This will be our budget line of pies which requires new branding/DIFFERENT feel from our current brand which is brown and red. I will attach an example of our current pie packaging which can be used for your graphic die line (example only).

This will be a Beef Flavoured pie, made by our bakery packed in plastic flow wrap packaging.

Our business called Brindle Vale is located in Papua New Guinea and we supply a wide range of premium imported, local and in-house manufactured products from our Butchery and Bakery. Our bakery produces cakes, pastries etc. and our pies are well known and sold wholesale, in our grocery store and at our quick service restaurant sites.

Target Audience: Budget, Value for Money product range. Our customers respond well to visual images rather than reading information, so keep it simple, bright, and striking.

Requirements:
• 1 x design front and back (see example for die line only, design should be different)
• 3-4 colours maximum. Colours that entice hunger e.g. yellow/orange
• Window areas – packaging should be at least 40% transparent (see the product)
• Area for barcode.
• Require to be fully editable in either AI/PSD format.

TEXT:

‘Velkoro Scholar Pie’ (Title)

‘Beef Flavoured Pie’ (Description)

‘Prepared with the highest quality ingredients and baked fresh, every day, just for you!’ (Comments)

‘Gudpela Kaikai Nau!’ (Fun advertising words to stand out)

‘We welcome your feedback or comments. Please contact us at www.bvx-example.com.pg’

‘ALLERGENS: Products containing wheat, nuts, sesame, soy, milk and egg are made in the Brindle Vale KTO Ltd Bakery. Products may contain gluten.’

‘STORAGE: Store in a cool dry place from direct sunlight.’

Thank you and look forward to collaborating on some great designs here :)

Target Market(s)

Budget, value for money, Papua New Guinea customers

Industry/Entity Type

Food Retail

Font styles to use
Sans Serif

Colors
FFF300
FFF600
FEFA6F
FFFEC7
FFFEE8
FFC000
F8CF3A
FAE287
FDF2CF
FEFAEE
F0912C
F2A743
F7CA91
FBE8D2
FDF5EE
EE7325
F08F49
F5BC92
FAE3D3
FDF4ED
EB3D1F
EC4F4E
F09395
F8D3D4
FCEDEE

Requirements
Must have
• Transparent window >40% of the packaging, 3-4 colours maximum, area for barcode
Nice to have
• Papua New Guinea theme details
Should not have
• Our Orrel Crumb Yard Logo (this is a new range of pies we want to market separately)

```html
<!DOCTYPE html>
<html lang="en">
<head>
<meta charset="utf-8">
<title>Velkoro Scholar Pie – Flow Wrap Front</title>
<link rel="stylesheet" href="https://fonts.googleapis.com/css2?family=Bebas+Neue&family=Yellowtail&family=Montserrat:wght@500&display=swap">
<style>
  :root {
    --orange: #ee7325;
    --orange-deep: #e0671f;
    --yellow: #fff300;
    --ink: #231f20;
    --white: #ffffff;
    --window-light: #fbfbfc;
    --window-shade: #e7e8ea;
  }
  html, body {
    margin: 0;
    padding: 0;
    width: 1200px;
    height: 1200px;
    overflow: hidden;
    background: var(--white);
  }
  .canvas {
    position: relative;
    width: 1200px;
    height: 1200px;
  }
  .pack-art,
  .text-layer {
    position: absolute;
    inset: 0;
  }
  .product-title {
    position: absolute;
    left: 224px;
    top: 512px;
    margin: 0;
    font-family: "Bebas Neue", sans-serif;
    font-weight: 400;
    font-size: 150px;
    line-height: 1;
    letter-spacing: 1px;
    color: var(--white);
    white-space: nowrap;
  }
  .product-sub {
    position: absolute;
    left: 226px;
    top: 628px;
    margin: 0;
    font-family: "Yellowtail", cursive;
    font-size: 84px;
    line-height: 1;
    color: var(--yellow);
    white-space: nowrap;
  }
  .description {
    position: absolute;
    left: 269px;
    top: 723px;
    margin: 0;
    font-family: "Montserrat", sans-serif;
    font-weight: 500;
    font-size: 18px;
    letter-spacing: 0.5px;
    color: var(--ink);
    white-space: nowrap;
  }
  .promise {
    position: absolute;
    left: 232px;
    top: 770px;
    margin: 0;
    font-family: "Yellowtail", cursive;
    font-size: 25px;
    line-height: 31px;
    color: var(--ink);
    white-space: nowrap;
  }
  .callout {
    position: absolute;
    left: 691px;
    top: 622px;
    width: 180px;
    margin: 0;
    text-align: center;
    font-family: "Yellowtail", cursive;
    font-size: 36px;
    line-height: 44px;
    color: var(--ink);
    transform: rotate(-8deg);
    white-space: nowrap;
  }
</style>
</head>
<body>
<main class="canvas">
  <svg class="pack-art" width="1200" height="1200" viewBox="0 0 1200 1200" aria-hidden="true">
    <defs>
      <clipPath id="pack-outline">
        <path d="M100,272 L114,272 C150,284 178,318 205,326 L600,350 L1010,352 C1040,322 1080,272 1119,272 L1119,940 C1080,940 1040,906 1010,900 L600,896 L205,898 C178,904 150,934 114,940 L100,940 Z"/>
      </clipPath>
      <linearGradient id="window-tone" x1="0" y1="0" x2="0" y2="1">
        <stop offset="0" stop-color="#e7e8ea"/>
        <stop offset="0.25" stop-color="#fbfbfc"/>
        <stop offset="0.75" stop-color="#fbfbfc"/>
        <stop offset="1" stop-color="#e7e8ea"/>
      </linearGradient>
    </defs>

    <g class="pack" clip-path="url(#pack-outline)">
      <rect class="window" x="90" y="260" width="1040" height="690" fill="url(#window-tone)"/>
      <path class="panel-edge" d="M619,250 L619,356 C655,392 672,430 672,469 L664,500 C716,510 758,548 778,596 L842,770 C850,820 842,880 825,950"
            fill="none" stroke="#fff300" stroke-width="16"/>
      <path class="panel" d="M90,250 L619,250 L619,356 C655,392 672,430 672,469 L664,500 C716,510 758,548 778,596 L842,770 C850,820 842,880 825,950 L90,950 Z"
            fill="#ee7325"/>
      <rect class="crimp-left" x="90" y="250" width="22" height="700" fill="#e0671f"/>
    </g>
    <path d="M100,272 L114,272 C150,284 178,318 205,326 L600,350 L1010,352 C1040,322 1080,272 1119,272 L1119,940 C1080,940 1040,906 1010,900 L600,896 L205,898 C178,904 150,934 114,940 L100,940 Z"
          fill="none" stroke="#e7e8ea" stroke-width="1.5"/>

    <g class="burst">
      <circle cx="782" cy="697" r="94" fill="#fff300"/>
      <circle cx="782" cy="697" r="99" fill="none" stroke="#fff300" stroke-width="12" stroke-dasharray="13 13"/>
    </g>
  </svg>

  <div class="text-layer">
    <h1 class="product-title">VELKORO</h1>
    <p class="product-sub">Scholar Pie</p>
    <p class="description">BEEF FLAVOURED PIE</p>
    <p class="promise">Prepared with the highest quality<br>ingredients and baked fresh, everyday,<br>just for you!</p>
    <p class="callout">Gudpela<br>Kaikai<br>Nau!</p>
  </div>
</main>
</body>
</html>
```